Wordpress Theme for Medical Clinics

** Please view updated Sitemap2.pdf doc to clarify some confusion ***

This is a multiuser WordPress subscription site for medical clinics. Please see attachment for sitemap. Please do not include extra content like social media icons, search bars, or images. If you have questions, please ask for clarification.
The site contains the following pages and sub-pages:

1. Home
2. Our Clinic
2a. Our Clinic > Mission
2b. Our Clinic > Services
2c. Our Clinic > Clinic Policies
2d. Our Clinic > Schedules
3. Our Staff
3a. Our Staff > [Staff member page]
4. Resources
4a. Resources > Patient Health (index)
4b. Resources > Patient Health (index) > [post]
4c. Resources > Links
4d. Resources > Forms
5. Alerts
5a. Alerts > [Alert Page]
6. Contact Us

Includes the Following Pages, Subpages, and Content
1. Home
a. About Us
b. Our Staff
c. Bulletins
d. Accepting New Patients (shown as an alert widget)
e. Links
i. Physician Toolbox
ii. Book an Appointment
f. Clinic Policies
i. Show first 3 policies (e.g. Late Arrivals, Missed Appointments, Fees)
ii. Link to Clinic Policies page
g. Primary widget (displayed on all pages)
i. Hours of operation
ii. Contact Info
1. Tel
2. Fax
3. Email
4. Address
5. Get directions (link to Google Maps)
2. Our Clinic
a. Main Page
i. Clinic Name
ii. Overview
iii. Languages Spoken
iv. Secondary Navigation
1. Mission
2. Services
3. Clinic Policies
4. Schedules (see attachment)
b. Our Clinic > Mission
c. Our Clinic > Services
i. For each service include service TITLE and DESCRIPTION
d. Our Clinic > Clinic Policies
i. For each policy include policy TITLE and DESCRIPTION
ii. Include the following policies in mockup
1. Late arrivals
2. Missed appointments
3. Fees for missed appointments
4. Referrals and follow-ups
5. Services not covered by RDV
6. Information for TQL patients
7. Medical Legal Reports
e. Our Clinic > Schedules
3. Our Staff
a. Main Page
i. Display a list of staff members. Include NAME and DESIGNATION
b. Our Staff > [Staff Name]
i. Include NAME, PICTURE, DESIGNATION, and BIO
4. Resources
a. Resources > Patient Health
i. Main Page
1. Posts (ordered by date)
a. Title
b. Summary
2. Side Navigation
a. Post Categories
ii. Patient Health > [post title]
1. Title
2. Post Category
3. Date
4. Author
5. Summary
6. Body
b. Resources > Links
1. Secondary Navigation - Categories
a. Sample Categories:
i. Local Services
ii. RDV and Drug Coverage
iii. Mental Health Resources
2. Category page
a. Include the following links in the 'Local Services' category
i. Hypertension clinics
ii. Home Care services
iii. Vaccine Clinics
c. Resources > Forms
i. Display a table with form TITLE and CATEGORY
ii. Side Navigation
1. Form Categories
a. Use the following sample Categories
i. Referrals
ii. Insurance
iii. Intake
iv. Discharge
v. Waivers
5. Alerts
a. Main page
i. List of all Alert posts
1. Include post TITLE as a link to the post
ii. Side Navigation
1. Alerts Archive
a. shown as Month + Number of posts
iii. Alerts > [Alert page]
1. Include TITLE, DATE, AUTHOR, BODY
6. Contact Us
a. Map
b. Hours of operation
c. Address
d. Phone number
e. Fax number
e. Fax number
f. Map
g. Email

Design notes:
- fixed width
- responsive (need designs for mobile, tablet, and desktop)
- simple, dark font, white background
- use Font Awesome icons where needed
- user adds own logo

Target Market(s)

Medical Clinics

Industry/Entity Type

Medical

Number of Pages Required

5+ page

Font styles to use
Serif
Sans Serif

Requirements
Must have
• Please keep designs very simple.
• Examples:
• https://www.quandrix.com/install
• http://www.tervolane.com/company/about-us
• http://brightnumberhub.org/
• http://www.vorn.com/
Should not have
• Minimal or no use of shadows and gradients

```html
<!DOCTYPE html>
<html lang="en">
<head>
<meta charset="utf-8">
<title>Larchview Clinic – Medical Clinic</title>
<link href="https://fonts.googleapis.com/css2?family=Lato:wght@400;700;900&display=swap" rel="stylesheet">
<style>
:root{
  --teal:#45b6d6;
  --ink:#333;
  --muted:#777;
  --page:#f2f2f2;
  --panel:#ececec;
  --row:#f7f7f7;
  --white:#fff;
  --line:#ddd;
  --pale-blue:#e3f3f9;
  --faint:#d2d2d2;
}
*{box-sizing:border-box;margin:0;padding:0}
html,body{width:724px;height:1200px;overflow:hidden}
body{background:var(--page);font-family:'Lato',Arial,sans-serif;color:var(--ink);position:relative;font-size:7px}
.abs{position:absolute}
a{color:var(--teal);text-decoration:none}

/* top bar */
.topbar-phone{left:93px;top:7px;font-size:7px;display:flex;align-items:center;gap:4px}
.topbar-mail{left:163px;top:7px;font-size:6.5px;color:var(--teal)}
.topbar-links{right:96px;top:7px;font-size:6.5px;display:flex;gap:10px}
.topbar-links span+span{border-left:1px solid #ccc;padding-left:10px}

/* header */
.header{left:90px;top:22px;width:540px;height:42px;background:var(--white)}
.brand{left:112px;top:32px;display:flex;align-items:center;gap:6px}
.brand-mark{width:9px;height:9px;background:var(--teal);display:block}
.brand-name{font-size:12px;font-weight:700;color:var(--ink)}
.brand-tag{left:112px;top:46px;font-size:6px;color:var(--muted)}
.nav{left:0;top:36px;font-size:6.5px;text-transform:uppercase;width:724px;height:16px}
.nav span{position:absolute;top:0;height:16px;line-height:16px;white-space:nowrap}
.nav .active{background:var(--teal);color:var(--white);padding:0 6px}

/* hero */
.hero{left:0;top:64px;width:724px;height:226px;background:linear-gradient(90deg,#d9cfc8 0%,#efeae6 25%,#f6f3f0 50%,#e6dcd3 70%,#d8cabd 100%)}
.hero-label{left:148px;top:108px;width:167px;height:22px;background:var(--teal);color:var(--white);font-size:11px;font-weight:700;padding:5px 9px}
.hero-text{left:148px;top:135px;width:214px;height:40px;background:var(--teal);color:var(--white);font-size:6px;line-height:10px;padding:6px 10px}
.hero-btn{left:148px;top:180px;width:50px;height:18px;border:1px solid var(--teal);color:var(--teal);background:rgba(255,255,255,.6);font-size:6.5px;font-weight:700;text-align:center;line-height:16px}
.hero-arrow{top:163px;width:24px;height:24px;border-radius:50%;background:#2a2a2a}
.hero-dots{left:584px;top:276px;display:flex;gap:3px}
.hero-dots i{width:8px;height:8px;border-radius:50%;border:1px solid var(--teal);background:var(--white)}
.hero-dots i:first-child{background:var(--teal)}

/* main */
.main{left:90px;top:290px;width:540px;height:703px;background:var(--white)}
.card-head{height:23px;background:var(--teal);color:var(--white);font-size:7px;font-weight:700;display:flex;align-items:center;gap:5px;padding-left:7px}
.card{background:var(--panel)}
.hours{left:116px;top:310px;width:156px;height:197px}
.hours-table{margin:12px 4px 0;width:148px;border-collapse:collapse;font-size:5.5px}
.hours-table td{height:18px;padding-left:8px;background:var(--white)}
.hours-table tr:nth-child(even) td{background:var(--row)}
.hours-table td:first-child{font-weight:700;width:73px}
.hours-table td:last-child{color:var(--muted)}
.holiday{margin:11px 0 0 13px;font-size:5.5px;color:var(--muted);text-decoration:underline}
.message{left:289px;top:310px;width:156px;height:197px}
.field{position:absolute;left:13px;width:134px;height:17px;background:var(--white);border:1px solid var(--line);font-size:5.5px;color:var(--muted);padding:4px 4px}
.field-icon{position:absolute;right:0;top:0;width:18px;height:15px;border-left:1px solid var(--line);display:flex;align-items:center;justify-content:center}
.submit{position:absolute;left:115px;top:171px;width:32px;height:17px;border:1px solid var(--teal);color:var(--teal);font-size:5.5px;text-align:center;line-height:15px;background:var(--white)}
.contact{left:461px;top:311px;width:157px;height:77px;background:var(--teal);color:var(--white);padding:7px 8px}
.contact h3{font-size:8.5px;font-weight:400;display:flex;gap:6px;align-items:center;margin-bottom:7px}
.contact dl{display:grid;grid-template-columns:64px 1fr;font-size:5.5px;line-height:8.5px}
.contact dt{font-weight:700}
.patients-photo{left:461px;top:402px;width:157px;height:56px;background:linear-gradient(120deg,#d8e4ea,#f1eeea 50%,#c9d5dc)}
.patients{left:461px;top:458px;width:157px;height:49px;background:var(--pale-blue);border-left:3px solid var(--teal);padding:11px 12px}
.patients h4{font-size:10px;font-weight:700;margin-bottom:5px}
.patients p{font-size:6.5px;color:var(--muted)}
.patients p a{color:var(--muted);text-decoration:underline}

.section-title{font-size:11px;font-weight:700;color:var(--ink)}
.doctor-photo{left:118px;top:545px;width:98px;height:135px;background:linear-gradient(180deg,#f4f4f4,#dfe6ea)}
.doctor-card{left:118px;top:680px;width:98px;height:32px;background:var(--panel);text-align:center;font-size:6px;padding-top:6px;line-height:10px}
.doctor-card em{color:var(--muted)}
.doctor-bar{left:227px;top:545px;width:153px;height:18px;background:var(--panel);font-size:6px;display:flex;align-items:center}
.doctor-bar .ico{width:18px;height:18px;background:var(--teal);display:flex;align-items:center;justify-content:center;margin-right:8px}
.doctor-bio{left:227px;top:569px;width:153px;font-size:5.5px;line-height:10.5px;color:var(--muted)}
.doctor-rule{left:227px;width:153px;height:1px;background:var(--line)}
.doctor-meta{left:227px;top:611px;font-size:5.5px;line-height:10px;color:var(--muted)}
.doctor-meta b{color:var(--ink)}
.days{left:227px;top:641px;font-size:6px}
.day-chip{left:278px;top:656px;width:18px;height:18px;background:var(--teal);color:var(--white);font-size:5px;text-align:center;line-height:18px}
.btn-solid{left:227px;top:694px;width:57px;height:18px;background:var(--teal);color:var(--white);font-size:6px;text-align:center;line-height:18px}
.btn-outline{left:349px;top:694px;width:57px;height:18px;border:1px solid var(--teal);color:var(--teal);font-size:6px;text-align:center;line-height:16px}
.see-all{left:122px;top:729px;font-size:7px;text-decoration:underline;color:var(--teal)}

.alert-item{left:122px;width:284px;height:18px;background:var(--panel);font-size:5.5px;font-weight:700;display:flex;align-items:center}
.alert-item .toggle{width:18px;height:18px;background:var(--teal);color:var(--white);font-size:10px;text-align:center;line-height:18px;margin-right:8px}
.alert-body{left:122px;top:815px;width:284px;height:47px;background:var(--panel);border-left:18px solid #d4d4d4;font-size:5.5px;line-height:10px;color:var(--muted);padding:5px 10px}

.why-photo{left:447px;top:552px;width:154px;height:74px;background:linear-gradient(120deg,#dfe8ec,#f3f2ef 55%,#cfd9df)}
.why-text{left:448px;top:636px;width:155px;font-size:5.5px;line-height:12px;color:var(--muted)}
.feature{left:448px;display:flex;gap:12px}
.feature .circle{width:40px;height:40px;border-radius:50%;background:var(--teal);border:2px solid #9fd8e9;display:flex;align-items:center;justify-content:center;flex:none}
.feature h5{font-size:6.5px;font-weight:700;margin:3px 0 5px}
.feature p{font-size:5.5px;line-height:10.5px;color:var(--muted)}
.policies{left:455px;top:870px;list-style:none;font-size:5.5px;line-height:13.7px}
.policies li{display:flex;align-items:center;gap:8px}
.policies li i{width:5px;height:5px;background:#555;display:block}
.view-all{left:450px;top:969px;font-size:5.5px;color:var(--muted);text-decoration:underline}

/* footer */
.foot-title{top:1014px;font-size:8px;color:#666}
.foot-list{top:1037px;list-style:none;font-size:5.5px;line-height:13.5px;color:#666}
.foot-list li::before{content:"›";margin-right:8px;font-weight:700;font-size:7px}
.foot-plain{font-size:6.5px;font-weight:700;color:#555;line-height:13.5px}
.foot-hours{left:336px;top:1037px;font-size:5.5px;line-height:10.5px;color:#666;border-collapse:collapse}
.foot-hours td:first-child{font-weight:700;width:48px;color:var(--ink)}
.foot-contact{left:486px;top:1036px;font-size:5.5px;line-height:10px;color:#666}
.foot-contact p{display:flex;align-items:center;gap:5px;margin-bottom:4px}
.foot-rule{left:116px;top:1155px;width:508px;height:1px;background:var(--line)}
.copyright{left:122px;top:1164px;font-size:5.5px;color:#666}
.legal{left:359px;top:1163px;display:flex;gap:9px;font-size:6px;color:var(--teal)}
.foot-brand{left:520px;top:1161px;display:flex;align-items:center;gap:5px}
.foot-brand .brand-mark{background:var(--faint)}
.foot-brand .brand-name{color:var(--faint)}
</style>
</head>
<body>

<div class="abs topbar-phone">
  <svg width="8" height="8" viewBox="0 0 8 8"><rect width="8" height="8" rx="1" fill="#333"/><path d="M2.3 1.8l1 1-.5.6a3.6 3.6 0 0 0 1.6 1.6l.6-.5 1 1-.7.7C3.6 6 2 4.4 1.6 2.5z" fill="#fff"/></svg>
  <span>780-555-0142</span>
</div>
<div class="abs topbar-mail">name@larchviewclinic.ca</div>
<div class="abs topbar-links"><span><a href="#">Book an Appointment</a></span><span><a href="#">Physical Toolbox</a></span></div>

<header class="abs header"></header>
<div class="abs brand"><span class="brand-mark"></span><span class="brand-name">Larchview Clinic</span></div>
<div class="abs brand-tag">Family Medicine &amp; Rehabilitation</div>
<nav class="abs nav">
  <span class="active" style="left:322px">Home</span>
  <span style="left:367px">Our Clinic</span>
  <span style="left:417px">Our Staff</span>
  <span style="left:470px">Resources</span>
  <span style="left:526px">Alerts</span>
  <span style="left:568px">Contact Us</span>
</nav>

<section class="abs hero" role="img" aria-label="Photo of a smiling nurse with a stethoscope holding a tablet, blurred clinic background"></section>
<div class="abs hero-label">FIRST THUMBNAIL LABEL</div>
<div class="abs hero-text">Vivamus mattis, magna sed tempor pellentesque, leo nisl condimentum enim, sed condimentum neque libero a ante. Nulla id orci nulla.</div>
<div class="abs hero-btn">KNOW MORE</div>
<div class="abs hero-arrow" style="left:97px"><svg width="24" height="24"><path d="M14 7l-5 5 5 5" stroke="#fff" stroke-width="2" fill="none"/></svg></div>
<div class="abs hero-arrow" style="left:600px"><svg width="24" height="24"><path d="M10 7l5 5-5 5" stroke="#fff" stroke-width="2" fill="none"/></svg></div>
<div class="abs hero-dots"><i></i><i></i><i></i></div>

<main class="abs main"></main>

<section class="abs card hours">
  <div class="card-head"><svg width="8" height="8"><circle cx="4" cy="4" r="3.3" stroke="#fff" fill="none"/><path d="M4 2v2h1.5" stroke="#fff" fill="none"/></svg>Hours of Operation</div>
  <table class="hours-table">
    <tr><td>Monday</td><td>09:00 am - 4:00 pm</td></tr>
    <tr><td>Tuesday</td><td>05:00 am - 10:00 pm</td></tr>
    <tr><td>Wednesday</td><td>Not Available</td></tr>
    <tr><td>Thursday</td><td>09:00 am - 4:00 pm</td></tr>
    <tr><td>Friday</td><td>09:00 am - 4:00 pm</td></tr>
    <tr><td>Saturday</td><td>09:00 am - 4:00 pm</td></tr>
    <tr><td>Sunday</td><td>Not Available</td></tr>
  </table>
  <div class="holiday">Holiday Hours</div>
</section>

<section class="abs card message">
  <div class="card-head"><svg width="8" height="8"><circle cx="4" cy="2.5" r="1.8" fill="#fff"/><path d="M1 8a3 3 0 0 1 6 0z" fill="#fff"/></svg>Send us a Message</div>
  <div class="field" style="top:36px">Select Department<span class="field-icon"><svg width="6" height="4"><path d="M0 0h6L3 4z" fill="#45b6d6"/></svg></span></div>
  <div class="field" style="top:63px">Your Name (required)</div>
  <div class="field" style="top:90px">Your Phone (required)</div>
  <div class="field" style="top:117px">Email (required)</div>
  <div class="field" style="top:144px">Date of Appointment<span class="field-icon"><svg width="7" height="7"><rect x=".5" y="1" width="6" height="5.5" stroke="#45b6d6" fill="none"/><path d="M.5 3h6" stroke="#45b6d6"/></svg></span></div>
  <div class="submit">SUBMIT</div>
</section>

<section class="abs contact">
  <h3><svg width="8" height="8"><rect width="8" height="8" rx="1" fill="#fff"/><path d="M2.3 1.8l1 1-.5.6a3.6 3.6 0 0 0 1.6 1.6l.6-.5 1 1-.7.7C3.6 6 2 4.4 1.6 2.5z" fill="#45b6d6"/></svg>Contact Inquiries</h3>
  <dl>
    <dt>Telephone:</dt><dd>780-555-0198</dd>
    <dt>Email:</dt><dd>contact@larchviewclinic.ca</dd>
    <dt>Address:</dt><dd>48 Larch Avenue<br>Red Deer, AB<br>Canada, T4N 2K7</dd>
  </dl>
</section>
<div class="abs patients-photo" role="img" aria-label="Photo of a doctor talking with an elderly patient"></div>
<section class="abs patients">
  <h4>NEW PATIENTS?</h4>
  <p>Accepting new patients. <a href="#">Contact us.</a></p>
</section>

<h2 class="abs section-title" style="left:118px;top:520px">Our Doctor Highlights</h2>
<div class="abs doctor-photo" role="img" aria-label="Portrait photo of a doctor in a white coat with a stethoscope"></div>
<div class="abs doctor-card"><b>Reed Halvorsen</b>, MPH<br><em>Medicine, Surgery</em></div>
<div class="abs doctor-bar"><span class="ico"><svg width="7" height="7"><circle cx="3.5" cy="2" r="1.7" fill="#fff"/><path d="M.5 7a3 3 0 0 1 6 0z" fill="#fff"/></svg></span><b>Reed Halvorsen</b>,&nbsp;<span style="color:var(--muted)">MPH</span></div>
<p class="abs doctor-bio">Saleem naijar kaasram eerie can be disbursed in the wofl like of a fox that is her thing smaoasa lase lemedds laasd pamade eleifend sapien.</p>
<div class="abs doctor-rule" style="top:606px"></div>
<div class="abs doctor-meta"><i>Medicine, Surgery</i><br><b>Email:</b> <a href="#">reedhalvorsen@mailbox.example</a></div>
<div class="abs doctor-rule" style="top:651px"></div>
<div class="abs days">Working Days</div>
<div class="abs day-chip">Mon</div>
<div class="abs btn-solid">PREV DOCTORS</div>
<div class="abs btn-outline">NEXT DOCTORS</div>
<a class="abs see-all" href="#">› See All Doctors</a>

<h2 class="abs section-title" style="left:122px;top:761px">Alerts</h2>
<div class="abs alert-item" style="top:797px"><span class="toggle">−</span>Alerts 1 Headline Goes Here</div>
<div class="abs alert-body">Consectetur adipiscing elit. Praesent pulvinar massa nec augue malesuada in aliquam odio interdum. Fusce vulputate eleifend sapien. Vestibulum purus quam, scelerisque ut, mollis sed, nonummy id, metus.</div>
<div class="abs alert-item" style="top:868px"><span class="toggle">+</span>Alerts 2 Headline Goes Here</div>
<div class="abs alert-item" style="top:891px"><span class="toggle">+</span>Alerts 3 Headline Goes Here</div>
<div class="abs alert-item" style="top:913px"><span class="toggle">+</span>Alerts 4 Headline Goes Here</div>

<h2 class="abs section-title" style="left:446px;top:520px">Why Our Clinic?</h2>
<div class="abs why-photo" role="img" aria-label="Photo of doctors attending to a patient in a hospital bed"></div>
<p class="abs why-text">Lorem ipsum dolor sit amet, consectetur adipiscing elit. Etiam quis placerat urna. Nulla nulla diam, adipiscing non ornare non, commodo. Lorem ipsum dolor sit amet, consectetur adipiscing elit. Etiam quis</p>
<div class="abs feature" style="top:698px">
  <span class="circle"><svg width="14" height="14"><rect x="3" y="1" width="8" height="12" stroke="#fff" fill="none"/><path d="M7 4v4M5 6h4" stroke="#fff"/></svg></span>
  <div><h5>Great Infrastructure</h5><p>Nunc at pretium est curabi-<br>tur commodo leac est</p></div>
</div>
<div class="abs feature" style="top:748px">
  <span class="circle"><svg width="16" height="12"><rect x="1" y="2" width="10" height="7" stroke="#fff" fill="none"/><path d="M11 4h3l1 3v2h-4M6 3.5v4M4 5.5h4" stroke="#fff" fill="none"/><circle cx="4" cy="10" r="1.3" fill="#fff"/><circle cx="12" cy="10" r="1.3" fill="#fff"/></svg></span>
  <div><h5>24/7 Ambulance Services</h5><p>Nunc at pretium est curabi-<br>tur commodo leac est</p></div>
</div>
<div class="abs feature" style="top:798px">
  <span class="circle"><svg width="14" height="12"><rect x="1" y="3" width="12" height="8" stroke="#fff" fill="none"/><path d="M5 3V1h4v2M7 5v4M5 7h4" stroke="#fff" fill="none"/></svg></span>
  <div><h5>Cutting Edge Technology</h5><p>Nunc at pretium est curabi-<br>tur commodo leac est</p></div>
</div>

<h2 class="abs section-title" style="left:450px;top:851px">Clinic Policies</h2>
<ul class="abs policies">
  <li><i></i><a href="#">Late Arrivals</a></li>
  <li><i></i><a href="#">Missed Appointments</a></li>
  <li><i></i><a href="#">Fees for Missed Appointments</a></li>
  <li><i></i><a href="#">Referrals and Follow-ups</a></li>
  <li><i></i><a href="#">Services Not Covered by RDV</a></li>
  <li><i></i><a href="#">Information for TQL patients</a></li>
  <li><i></i><a href="#">Medical Legal Reports</a></li>
</ul>
<div class="abs view-all">View All</div>

<footer>
  <div class="abs foot-title" style="left:122px">OUR CLINIC</div>
  <ul class="abs foot-list" style="left:122px">
    <li><a href="#">Mission</a></li><li>Services</li><li>Schedules</li><li>Policies</li>
  </ul>
  <div class="abs foot-plain" style="left:122px;top:1094px">STAFF<br>ALERTS<br>CONTACT US</div>

  <div class="abs foot-title" style="left:231px">RESOURCES</div>
  <ul class="abs foot-list" style="left:231px">
    <li><a href="#">Our Clinic</a></li><li>Mission</li><li>Services</li><li>Policies</li>
  </ul>

  <div class="abs foot-title" style="left:336px">HOURS OF OPERATION</div>
  <table class="abs foot-hours">
    <tr><td>Monday</td><td>09:00 am - 4:00 pm</td></tr>
    <tr><td>Tuesday</td><td>05:00 am - 10:00 pm</td></tr>
    <tr><td>Wednesday</td><td>Not Available</td></tr>
    <tr><td>Thursday</td><td>09:00 am - 4:00 pm</td></tr>
    <tr><td>Friday</td><td>09:00 am - 4:00 pm</td></tr>
    <tr><td>Saturday</td><td>09:00 am - 4:00 pm</td></tr>
    <tr><td>Sunday</td><td>Not Available</td></tr>
    <tr><td colspan="2" style="font-weight:400;text-decoration:underline;color:#666">Holiday Hours</td></tr>
  </table>

  <div class="abs foot-title" style="left:486px">CONTACT US</div>
  <div class="abs foot-contact">
    <p style="display:block;margin-bottom:8px">48 Larch Avenue, Red Deer, AB<br>Canada, T4N 2K7</p>
    <p><svg width="6" height="6"><path d="M1.2 .6l1.2 1.2-.6.7a3.5 3.5 0 0 0 1.7 1.7l.7-.6 1.2 1.2-.8.8C2.5 5 1 3.4.5 1.4z" fill="#555"/></svg><b>Phone :</b> 1780-555-0198</p>
    <p><svg width="7" height="5"><rect width="7" height="5" fill="#555"/><path d="M0 0l3.5 3L7 0" stroke="#fff" stroke-width=".7" fill="none"/></svg><b>Email :</b> <a href="#">info@larchviewclinic.ca</a></p>
    <p><svg width="6" height="6"><circle cx="3" cy="3" r="3" fill="#555"/></svg><b>Website :</b> <a href="#">www.larchviewclinic.ca</a></p>
  </div>

  <div class="abs foot-rule"></div>
  <div class="abs copyright">Copyright © 2015 Larchview Clinic Healthcare Solutions. All Rights Reserved |</div>
  <div class="abs legal"><span>Terms</span><span>Privacy Policy</span><span>Legal Agreement</span></div>
  <div class="abs foot-brand"><span class="brand-mark"></span><span class="brand-name">Larchview Clinic</span></div>
</footer>

</body>
</html>
```